Stretch on the Green with Mara

I want to advertise my Stretch on the Green classes for Summer. Classes are outside at the lovely local park. Dunmore field. 82 Halcombe St. Westlow.
Classes are for beginners to advance levels.
Classes start Monday, October 17th.
Monday 6pm Beginners
Tuesday 6pm Intermediate
Thursday 6pm Intermediate/Advance
Saturday 9am All fitness levels
My Pilates classes are specially designed to help improve strength and flexibility but as well will also improve posture, reduce stress and develop control and endurance in the entire body.
Booking essential. Limited numbers so I can make sure the correct technique is always being followed.
For more info or to book contact details:
Mara 027385916
mara@corestudiomara.net
www.corestudiomara.net
$15 Per Session

Target Market(s)

Males and Females ages 35plus.

Industry/Entity Type

Fitness

Font styles to use
Sans Serif

Requirements
Must have
• My logo. Contact details. A Park that looks lovely to exercise at.
Nice to have
• Summer looking. Trees - inspiration to be exercising outside

```html
<!DOCTYPE html>
<html lang="en">
<head>
<meta charset="utf-8">
<title>Stretch on the Green – Classes for Summer</title>
<link rel="stylesheet" href="https://fonts.googleapis.com/css2?family=Montserrat:wght@300;400;600;700;800;900&display=swap">
<style>
  :root {
    --charcoal: #464647;
    --pink: #e6428b;
    --pink-soft: #f08ab4;
    --pink-icon: #f7b6d1;
    --ink: #2f2f31;
    --paper: #ffffff;
    --rule: #d9d9d9;
    --backdrop: #e9e4d8;
    --grass-light: #c9e26a;
    --grass-deep: #7fa83a;
  }
  * { box-sizing: border-box; margin: 0; padding: 0; }
  html, body { width: 1200px; height: 900px; overflow: hidden; }
  body {
    background: var(--backdrop);
    font-family: "Montserrat", Arial, sans-serif;
    color: var(--ink);
    display: flex; align-items: center; justify-content: center;
  }
  .flyer {
    position: relative;
    width: 600px; height: 860px;
    background: var(--paper);
    overflow: hidden;
  }
  .masthead {
    position: absolute; left: 0; top: 0; width: 100%; height: 240px;
    background: var(--charcoal);
  }
  .brand {
    position: absolute; right: 34px; top: 28px;
    display: flex; align-items: center; gap: 8px;
    color: var(--pink-soft); font-weight: 400; font-size: 15px; letter-spacing: 1.5px; text-transform: uppercase;
  }
  .brand-dot { width: 10px; height: 10px; border-radius: 50%; background: var(--pink-soft); }
  .headline {
    position: absolute; left: 36px; top: 62px;
    color: #fff; font-weight: 900; text-transform: uppercase;
    font-size: 62px; line-height: 0.92; letter-spacing: -1px;
  }
  .subhead {
    position: absolute; left: 40px; top: 190px;
    color: #fff; font-weight: 800; font-size: 26px; text-transform: uppercase; letter-spacing: 0.5px;
  }
  .details-strip {
    position: absolute; left: 0; top: 240px; width: 100%; height: 32px;
    background: var(--pink); color: #fff;
    display: flex; align-items: center; gap: 8px; padding-left: 34px;
    font-size: 12.5px; font-weight: 700;
  }
  .details-strip svg { width: 12px; height: 12px; flex: none; }
  .details-strip sup { font-size: 8px; }
  .park-photo {
    position: absolute; left: 0; top: 272px; width: 100%; height: 288px;
    background: radial-gradient(ellipse at 50% 30%, #f1f6c4 0%, var(--grass-light) 40%, var(--grass-deep) 100%);
  }
  .info-card {
    position: absolute; left: 56px; top: 450px; right: 0; height: 280px;
    background: var(--paper);
  }
  .info-lower {
    position: absolute; left: 0; top: 560px; width: 100%; height: 170px; background: var(--paper);
  }
  .levels-title {
    position: absolute; left: 84px; top: 470px;
    font-size: 15px; font-weight: 800; text-transform: uppercase; letter-spacing: 0.2px;
  }
  .levels-rule { position: absolute; left: 84px; top: 494px; width: 470px; height: 2px; background: var(--pink); }
  .schedule { position: absolute; left: 84px; top: 504px; width: 230px; list-style: none; }
  .schedule li { padding: 6px 0 7px; border-bottom: 1px solid var(--rule); font-size: 16px; line-height: 1.1; }
  .schedule li:last-child { border-bottom: 0; }
  .schedule .day { font-weight: 400; display: block; }
  .schedule .level { font-weight: 800; display: block; }
  .about {
    position: absolute; left: 330px; top: 510px; width: 240px;
    font-size: 13px; line-height: 1.32; font-weight: 400;
  }
  .price-box {
    position: absolute; left: 334px; top: 662px; width: 232px; height: 84px;
    border: 5px solid var(--pink); background: var(--paper);
    display: flex; align-items: center; justify-content: center; gap: 10px;
    z-index: 2;
  }
  .price-amount { font-size: 50px; font-weight: 900; letter-spacing: -1px; }
  .price-divider { width: 2px; height: 48px; background: var(--rule); }
  .price-unit { font-size: 20px; font-weight: 800; line-height: 1; }
  .footer {
    position: absolute; left: 0; bottom: 0; width: 100%; height: 130px;
    background: var(--pink); color: #fff;
  }
  .cta {
    position: absolute; left: 40px; top: 36px;
    font-size: 20px; font-weight: 400; line-height: 1.12; text-transform: uppercase;
  }
  .contact { position: absolute; left: 318px; top: 22px; list-style: none; }
  .contact li { display: flex; align-items: center; gap: 8px; font-size: 14.5px; font-weight: 400; line-height: 1.5; }
  .contact li.phone { font-size: 28px; font-weight: 800; line-height: 1.3; }
  .contact svg { width: 13px; height: 13px; flex: none; }
  .contact li.phone svg { width: 16px; height: 16px; }
</style>
</head>
<body>
<main class="flyer">
  <header class="masthead">
    <div class="brand"><span class="brand-dot"></span>Core Studio Mara</div>
    <h1 class="headline">Stretch on<br>the Green</h1>
    <p class="subhead">Classes for Summer</p>
  </header>

  <div class="details-strip">
    <svg viewBox="0 0 12 12"><path d="M6 0.5a4 4 0 0 1 4 4c0 3-4 7-4 7s-4-4-4-7a4 4 0 0 1 4-4z" fill="#fff"/><circle cx="6" cy="4.5" r="1.4" fill="#e6428b"/></svg>
    <span>Dunmore field. 82 Halcombe St. Westlow.</span>
    <svg viewBox="0 0 12 12"><rect x="1" y="2" width="10" height="9" rx="1" fill="none" stroke="#fff" stroke-width="1.2"/><line x1="1" y1="4.5" x2="11" y2="4.5" stroke="#fff" stroke-width="1.2"/></svg>
    <span>Monday, October 17<sup>th</sup></span>
  </div>

  <div class="park-photo" role="img" aria-label="Photo of two runners on a path through a sunny green park with trees"></div>

  <section class="info-card"></section>
  <div class="info-lower"></div>
  <h2 class="levels-title">Classes are for beginners to advance levels.</h2>
  <div class="levels-rule"></div>

  <ul class="schedule">
    <li><span class="day">Monday 6pm</span><span class="level">Beginners</span></li>
    <li><span class="day">Tuesday 6pm</span><span class="level">Intermediate</span></li>
    <li><span class="day">Thursday 6pm</span><span class="level">Intermediate/Advance</span></li>
    <li><span class="day">Saturday 9am</span><span class="level">All fitness levels</span></li>
  </ul>

  <p class="about">My Pilates classes are specially designed to help improve strength and flexibility but as well will also improve posture, reduce stress and develop control and endurance in the entire body.</p>

  <div class="price-box">
    <span class="price-amount">$15</span>
    <span class="price-divider"></span>
    <span class="price-unit">Per<br>Session</span>
  </div>

  <footer class="footer">
    <p class="cta">For more info<br>or to book<br>get intouch</p>
    <ul class="contact">
      <li class="phone"><svg viewBox="0 0 16 16"><path d="M3 1l3 0 1.2 3.5-2 1.3a9 9 0 0 0 5 5l1.3-2L15 10v3a2 2 0 0 1-2 2C7 15 1 9 1 3a2 2 0 0 1 2-2z" fill="#f7b6d1"/></svg>027385916</li>
      <li><svg viewBox="0 0 13 13"><rect x="0.8" y="2.5" width="11.4" height="8" fill="none" stroke="#f7b6d1" stroke-width="1.1"/><path d="M1 3l5.5 4 5.5-4" fill="none" stroke="#f7b6d1" stroke-width="1.1"/></svg>mara@corestudiomara.net</li>
      <li><svg viewBox="0 0 13 13"><circle cx="6.5" cy="6.5" r="5.6" fill="none" stroke="#f7b6d1" stroke-width="1.1"/><ellipse cx="6.5" cy="6.5" rx="2.4" ry="5.6" fill="none" stroke="#f7b6d1" stroke-width="1"/><line x1="0.9" y1="6.5" x2="12.1" y2="6.5" stroke="#f7b6d1" stroke-width="1"/></svg>www.corestudiomara.net</li>
    </ul>
  </footer>
</main>
</body>
</html>
```